Fleur Vallon Riding School Flyer Design

We need a flyer for our Horse riding school, called Fleur Vallon Riding School.

At Fleur Vallon Riding School, Horses and ponies are carefully matched to suit each rider's experience, ability and confidence. I am a Qualified instructor, equipped to train all levels from nervous beginners to the more advanced.

Horse riding is fun! Riders, particularly children, are taught not only skills on the horse, but skills that are integral to good horsemanship and ownership of horses.

We regularly host Ladies Days, Guest Instructors, 1 hour Trail Rides and Pony Ride Days!

We teach people how to interact safely with, and care for horses so they develop a genuine love and respect for the animals and the sport.

In addition to fundamental riding techniques including walk, trot, and canter, we teach our students:
Grooming and Care of horses, Safety around horses, Balance and Co-Ordination, How to saddle up and care for Tack, Responsibility for equipment and horse, Confidence and Confidence Building for all Ages.

Private and group lessons start at 5 years of age upwards.

We recommend children 4 years and under partake in 15 minute pony rides, mainly due to their attention span!

```html
<!DOCTYPE html>
<html lang="en">
<head>
<meta charset="utf-8">
<title>Fleur Vallon Riding School</title>
<link href="https://fonts.googleapis.com/css2?family=Raleway:wght@300;400&family=Open+Sans:wght@400;600&family=Roboto+Condensed:wght@400&display=swap" rel="stylesheet">
<style>
  :root {
    --ink-dark: #27302f;
    --ink-mid: #3c4746;
    --paper: #ffffff;
    --soft-white: #eef1ee;
    --photo-sky: #b9c0bd;
    --photo-ground: #8a918e;
    --photo-shadow: #1f2625;
  }
  html, body {
    margin: 0;
    padding: 0;
    width: 851px;
    height: 1200px;
    overflow: hidden;
    background: var(--ink-dark);
  }
  .flyer {
    position: relative;
    width: 851px;
    height: 1200px;
    overflow: hidden;
    background: linear-gradient(180deg, var(--ink-mid) 0%, var(--ink-dark) 45%, var(--ink-dark) 60%);
    color: var(--paper);
    font-family: "Open Sans", Arial, sans-serif;
  }
  .scene-photo {
    position: absolute;
    left: 0;
    top: 660px;
    width: 851px;
    height: 540px;
    background:
      radial-gradient(ellipse at 60% 85%, var(--photo-shadow) 0%, rgba(31,38,37,0.6) 18%, rgba(31,38,37,0) 40%),
      linear-gradient(180deg, var(--ink-dark) 0%, #58625f 25%, var(--photo-sky) 55%, var(--photo-ground) 80%, #6d7471 100%);
  }
  .brand {
    position: absolute;
    top: 22px;
    left: 0;
    width: 851px;
    text-align: center;
  }
  .brand-mark {
    display: block;
    margin: 0 auto;
  }
  .brand-name {
    margin: 40px 0 0;
    font-family: "Raleway", Arial, sans-serif;
    font-weight: 400;
    font-size: 32px;
    line-height: 1;
    letter-spacing: 8px;
    text-transform: uppercase;
  }
  .brand-tag {
    margin: 10px 0 0;
    font-family: "Raleway", Arial, sans-serif;
    font-weight: 400;
    font-size: 12px;
    letter-spacing: 4px;
    text-transform: uppercase;
  }
  .intro {
    position: absolute;
    top: 282px;
    left: 156px;
    width: 612px;
    font-size: 16px;
    line-height: 20px;
  }
  .intro p { margin: 0 0 20px; }
  .intro p:last-child { margin-bottom: 0; }
  .skills {
    list-style: none;
    margin: 0 0 20px;
    padding: 0 0 0 96px;
  }
  .divider {
    position: absolute;
    top: 642px;
    left: 80px;
    width: 690px;
    border-top: 3px dotted var(--soft-white);
  }
  .events {
    position: absolute;
    top: 652px;
    left: 80px;
    width: 700px;
    margin: 0;
    font-size: 15px;
    line-height: 20px;
    font-weight: 600;
    white-space: nowrap;
    color: var(--soft-white);
  }
  .call {
    position: absolute;
    left: 70px;
    top: 1124px;
    margin: 0;
    font-family: "Roboto Condensed", Arial, sans-serif;
    font-size: 32px;
    line-height: 40px;
    color: var(--paper);
  }
</style>
</head>
<body>
<main class="flyer">
  <div class="scene-photo" role="img" aria-label="Black and white photo of a dark horse standing beside a white wooden paddock fence"></div>

  <header class="brand">
    <svg class="brand-mark" width="120" height="120" viewBox="0 0 120 120" aria-hidden="true">
      <circle cx="60" cy="60" r="54" fill="none" stroke="#ffffff" stroke-width="3"/>
    </svg>
    <h1 class="brand-name">Fleur Vallon</h1>
    <p class="brand-tag">Riding School</p>
  </header>

  <section class="intro">
    <p>We teach people how to interact safely with, and care for horses so they develop a genuine love and respect for the animals and the sport.</p>
    <p>In addition to fundamental riding techniques including walk, trot, and canter, we teach our students:</p>
    <ul class="skills">
      <li>Grooming and Care of horses</li>
      <li>Safety around horses</li>
      <li>Balance and Coordination</li>
      <li>How to saddle up and care for Tack</li>
      <li>Responsibility for equipment and horse</li>
      <li>Confidence and Confidence Building for all Ages.</li>
    </ul>
    <p>Private and group lessons start at 5 years of age upwards. We recommend children 4 years and under partake in 15 minute pony rides, mainly due to their attention span!</p>
  </section>

  <div class="divider"></div>
  <p class="events">Ask about Ladies Days, Guest Instructors, 1 hour Trail Rides and Pony Ride Days!</p>

  <p class="call">Call 1-800-555-0142</p>
</main>
</body>
</html>
```